White Dove Release Postcard for Event Planners

We require a double-sided Postcard (8.5" x 5.5") that will be mailed to Event Planners advising them of our White Dove Release services for weddings, anniversaries, and other happy events.

Wingsong Moments is the originator of White Dove Releases in the greater Toronto area, adding a beautiful moment to weddings and other celebrations since 1995.

A professional release of Pure White Doves is a natural part of wedding ceremonies, lending a special celebratory note to the exchange of vows. White Doves are the living symbol of everlasting love, fidelity, peace and harmony. These lovely birds mate for life, building a home and raising their young together.

For more information, please visit www.wingsongmoments.example

Target Market(s)

Event and Wedding Planners. Primarily for weddings but could be for other types of celebratory events.

Industry/Entity Type

Events

Requirements
Must have
• Space for address label and stamp to be affixed.
• Pictures of beautiful brides with doves (see attachments).
Nice to have
• Multicultural weddings / brides
Should not have
• No religious images. Must be non-denominational.

```html
<!DOCTYPE html>
<html lang="en">
<head>
<meta charset="utf-8">
<title>Wingsong Moments – Postcard</title>
<link href="https://fonts.googleapis.com/css2?family=Cinzel:wght@400;700&family=Alegreya:ital@1&family=Roboto+Condensed:wght@400;700&family=Roboto:wght@400;700&family=Cabin&display=swap" rel="stylesheet">
<style>
  :root {
    --page-bg: #ecebe8;
    --marble-light: #f7f6f4;
    --marble-mid: #e6e4e2;
    --ink: #1f1f1f;
    --ink-soft: #3b3b3b;
    --script-blue: #2f3c9a;
    --script-purple: #4b1f63;
    --rule: #555;
    --photo-green: #5f7a4a;
    --photo-dark: #2b2e31;
    --photo-white: #e9e8ea;
    --dove-grey: #cfd0d3;
  }
  * { box-sizing: border-box; margin: 0; padding: 0; }
  html, body { width: 923px; height: 1200px; overflow: hidden; }
  body { background: var(--page-bg); position: relative; font-family: "Roboto Condensed", sans-serif; color: var(--ink); }

  .postcard {
    position: absolute; width: 763px; height: 495px; overflow: hidden;
    background: radial-gradient(ellipse at 70% 40%, var(--marble-light), var(--marble-mid) 90%);
  }
  .postcard--front { left: 37px; top: 53px; }
  .postcard--back { left: 101px; top: 643px; }

  .photo { position: absolute; }
  .photo--front-couple {
    left: 0; top: 0; width: 435px; height: 440px;
    background: radial-gradient(ellipse at 55% 55%, var(--photo-white) 0 18%, var(--photo-dark) 30%, var(--photo-green) 50%, rgba(230,228,226,0) 72%);
  }
  .photo--back-couple {
    left: 0; top: 0; width: 262px; height: 235px;
    background: linear-gradient(100deg, var(--photo-dark) 0 20%, var(--photo-white) 30% 55%, #5466a8 65%, var(--photo-green) 85%, rgba(230,228,226,0));
  }
  .illustration-dove {
    position: absolute;
    background: radial-gradient(ellipse, var(--dove-grey), rgba(207,208,211,0) 70%);
  }
  .postcard--front .illustration-dove { left: 15px; top: 3px; width: 140px; height: 150px; }
  .postcard--back .illustration-dove { left: 245px; top: 0; width: 140px; height: 160px; }

  .brand { position: absolute; text-align: center; width: 340px; font-family: "Cinzel", serif; }
  .postcard--front .brand { left: 418px; top: 22px; }
  .postcard--back .brand { left: 394px; top: 13px; }
  .brand__parent { font-size: 12px; letter-spacing: .5px; color: var(--ink-soft); }
  .brand__name { font-size: 27px; font-weight: 700; line-height: 1.05; color: var(--ink); letter-spacing: 1px; }
  .brand__services { font-size: 10.5px; font-weight: 700; margin-top: 2px; }
  .brand__region { font-size: 10px; color: var(--ink-soft); }

  .tagline { position: absolute; text-align: center; font-family: "Alegreya", serif; font-style: italic; line-height: 1.2; }
  .postcard--front .tagline { left: 430px; top: 122px; width: 330px; }
  .postcard--back .tagline { left: 405px; top: 98px; width: 330px; }
  .tagline .sm { font-size: 19px; color: var(--script-blue); }
  .tagline .lg { font-size: 26px; color: var(--script-purple); }
  .tagline .lg.blue { color: var(--script-blue); }

  .benefits { position: absolute; list-style: none; font-size: 12.5px; color: var(--ink-soft); }
  .benefits li { position: relative; padding-left: 18px; }
  .benefits li::before { content: "•"; position: absolute; left: 2px; }
  .postcard--front .benefits { left: 460px; top: 268px; }
  .postcard--front .benefits li { height: 24px; }
  .benefits .accent { font-size: 17px; font-weight: 700; color: var(--ink); }
  .postcard--back .benefits { left: 22px; top: 255px; font-size: 13.5px; color: var(--ink); }
  .postcard--back .benefits li { height: 21px; }

  .front-strap { position: absolute; left: 22px; top: 430px; font-family: "Cabin", sans-serif; font-size: 17px; line-height: 1.3; color: var(--ink-soft); }
  .front-contact { position: absolute; left: 351px; top: 440px; font-family: "Roboto", sans-serif; font-size: 25px; color: var(--ink-soft); }
  .front-contact strong { font-size: 36px; font-weight: 700; color: var(--ink); }

  .back-heading { position: absolute; left: 22px; top: 234px; font-size: 13.5px; font-weight: 700; }
  .care-note { position: absolute; left: 22px; top: 414px; width: 430px; font-size: 11.5px; line-height: 1.35; color: var(--ink); }
  .stamp-box { position: absolute; top: 217px; width: 102px; height: 66px; border: 1.5px solid var(--ink); background: #fff; }
  .stamp-box--one { left: 497px; }
  .stamp-box--two { left: 619px; }
  .address-label { position: absolute; left: 506px; top: 305px; font-size: 13px; }
  .address-line { position: absolute; left: 529px; width: 182px; border-bottom: 1.5px dotted var(--ink); }
  .divider { position: absolute; left: 22px; top: 452px; width: 722px; border-top: 1px solid var(--rule); }
  .back-contact { position: absolute; left: 22px; top: 457px; font-family: "Roboto", sans-serif; font-size: 17.5px; color: var(--ink-soft); }
  .back-contact strong { color: var(--ink); }
</style>
</head>
<body>

<section class="postcard postcard--front">
  <div class="photo photo--front-couple" role="img" aria-label="Photo of a bride and groom each holding a white dove at an outdoor ceremony"></div>
  <div class="illustration-dove" role="img" aria-label="Illustration of a white dove in flight"></div>

  <header class="brand">
    <p class="brand__parent">Silverfeather Worldwide</p>
    <h1 class="brand__name">WINGSONG MOMENTS</h1>
    <p class="brand__services">Weddings • Life Celebrations • Private &amp; Public Events</p>
    <p class="brand__region">Serving Southern Ontario Since 1995</p>
  </header>

  <p class="tagline">
    <span class="sm">White Doves for </span><span class="lg blue">Weddings</span><span class="sm"> and</span><br>
    <span class="lg">Other Celebrations</span><br>
    <span class="sm">The memory of a </span><span class="lg blue">White Dove</span><br>
    <span class="sm">Event lasts forever</span>
  </p>

  <ul class="benefits">
    <li>A natural part of wedding ceremonies…</li>
    <li style="list-style:none"><span class="accent">white doves</span> mate for life</li>
    <li>Symbolizes everlasting love, fidelity, peace and harmony</li>
    <li>Animal-friendly and environmentally conscientious</li>
    <li>In keeping with today’s values and concerns</li>
    <li>Non-denominational; multi-cultural appeal</li>
    <li>Professional staff, always on time</li>
  </ul>

  <p class="front-strap">Adding a special moment to special<br>events for more than 15 years</p>
  <p class="front-contact">Contact us : <strong>416-555-0142</strong></p>
</section>

<section class="postcard postcard--back">
  <div class="photo photo--back-couple" role="img" aria-label="Photo of a bride and groom holding white doves with a guest beside them"></div>
  <div class="illustration-dove" role="img" aria-label="Illustration of a white dove in flight"></div>

  <header class="brand">
    <p class="brand__parent">Silverfeather Worldwide</p>
    <h2 class="brand__name">WINGSONG MOMENTS</h2>
    <p class="brand__services">Weddings • Life Celebrations • Private &amp; Public Events</p>
    <p class="brand__region">Serving Southern Ontario Since 1995</p>
  </header>

  <p class="tagline">
    <span class="sm">White Doves for </span><span class="lg blue">Weddings</span><span class="sm"> and</span><br>
    <span class="lg">Other Celebrations</span><span class="sm"> The memory of a</span><br>
    <span class="lg">White Dove</span><span class="sm"> Event lasts forever</span>
  </p>

  <p class="back-heading">Adding a special moment to special events for more than 15 years</p>
  <ul class="benefits">
    <li>A natural part of wedding ceremonies… white doves mate for life</li>
    <li>Symbolizes everlasting love, fidelity, peace and harmony</li>
    <li>Animal-friendly and environmentally conscientious</li>
    <li>In keeping with today’s values and concerns</li>
    <li>Non-denominational; multi-cultural appeal</li>
    <li>Professional staff, always on time</li>
    <li>Easy coordination with photographers/videographers</li>
  </ul>
  <p class="care-note">Our White Doves receive the best of care and are fully trained to return to their dovecote upon their release from distances of more than 150 kilometres away.</p>

  <div class="stamp-box stamp-box--one"></div>
  <div class="stamp-box stamp-box--two"></div>
  <p class="address-label">To,</p>
  <div class="address-line" style="top:318px;left:520px;width:191px"></div>
  <div class="address-line" style="top:347px"></div>
  <div class="address-line" style="top:374px"></div>
  <div class="address-line" style="top:401px"></div>

  <div class="divider"></div>
  <p class="back-contact">For more information, please contact <strong>Elena</strong> info@wingsongmoments.example | 416-555-0142</p>
</section>

</body>
</html>
```